依頼詳細
・アルミパウチパッケージの300mlタイプ。シンプルでありながら、女性の可愛らしさとオシャレ感漂うデザイン希望。ビーチ味なので、色はピンク系が希望だが、ピンク×白(マット系)が映えるのではないかと思われますが、使用する色の割合によってイメージが変わると思います。センスあれば色は気にせず自由にデザインください。
・何色使用するかですが、シンプルに2色~3色が良いかと思います。
・サイズに関しては、縦165mm×横84mm(折り目部分や貼付け部分を別途ファイル添付)

記載項目
サイズ縦165mm×横84mm。パッケージ素材はアルミパウチ、表面は「MAKIRO」のネーミング文字、「賞味期限」は指定位置に入れてください。
※詳細は、添付ファイルをご参照ください。
希望イメージ
• +5 0 +5
• シンプル
複雑
• 単色
カラフル
• 暗い
明るい
• 日常
高級
• 遊び心
厳粛
• 未来的
伝統的
• 女性的
男性的
希望する色
赤系
納品ファイル
• イラストレーター形式 (.ai)
補足説明
依頼公開後の追記内容
報酬金額をアップし、より多くのご提案をいただきたく、要望に合ったデザインを期待しております。ランサーの方々、何卒よろしくお願いいたします。
報酬金額をアップ致しましたので、より多くのご提案をいただき、要望に適ったデザインが、ランサーの方々より送られてくることを期待しております。何卒、宜しくお願いいたします。
ランサーの方々より延長依頼のご要望がございましたのと、もう少しデザイン提案が欲しいので延長させていただきました。
かなりクオリティの高いデザインを数多くご提案いただき検討致しましたが、「これだ!」という「インパクトある№1デザイン」がないため、2日間延長させていただきます。シャンプーに見えてしまうデザインが多い気がします。
【ヒアルロン酸、コラーゲン等の美容飲料】のイメージを再度ご考慮いただければ幸いです!!
デザイン決定後、弊社は12/29~1/6まで年末年始休業のため、年始の1/7以降に細部等のご相談をさせていただきたいと存じます。裏面の文面等もご相談させていただく予定ですので、何卒宜しくお願いいたします。
ランサーの皆様、数多くのご提案を賜り心より感謝申し上げます。想定以上の際立った素晴らしいデザインがあり、大変嬉しく存じます。弊社は年末年始の休業期間となり、やり取りが出来なくなりますため最大延長(1/6日まで)をさせていただきます。
年始は1/7(月)より、新たにやり取りをさせていただきたく存じます。
その際は、ご対応の程 何卒よろしくお願いいたします。
それでは皆様、良いお年をお迎えください。
感謝
■ 選んだ理由

デザインが、気品と可愛さもあり、素敵な女性がこの商品を手にしているイメージが湧き、女性社員からも多くの賛同をいただいたため最終的にこのデザインに決定させていただきました。また、ぷるるん感も可愛く表現され、色使いもきれいなピンクで、成分表示もわかり易くて、高級感も漂いニーズに合致したものだったので、選定させていただきました。
また、こちらのランサー様は、度重なる細部の修正にも的確且つ迅速にご対応いただきましたことに心より御礼申し上げます。本当に、ありがとうございました。

■ 提案者全員のお礼・コメント

全80提案で、多くのランサーの方々よりデザインをいただき心より感謝しております。今回は、採用されなかったランサーの皆様、真摯なご対応ありがとうございました。また別の機会の際は、何卒よろしくお願いいたします。御礼まで。

```html
<!DOCTYPE html>
<html lang="ja">
<head>
<meta charset="utf-8">
<title>MAKIRO ヒアルロン酸入りゼリー飲料</title>
<link rel="stylesheet" href="https://fonts.googleapis.com/css2?family=Cormorant+Garamond:wght@500;600&family=Noto+Serif+JP:wght@500;700&family=Kosugi+Maru&display=swap">
<style>
  :root {
    --navy: #2b3a6e;
    --pink: #e88aa7;
    --pink-deep: #d9668c;
    --pink-soft: #f7d3de;
    --peach-light: #fbe3e9;
    --peach-mid: #f2aec0;
    --paper: #fdfbfc;
    --white: #ffffff;
  }
  * { margin: 0; padding: 0; box-sizing: border-box; }
  html, body { width: 1200px; height: 2496px; overflow: hidden; background: var(--paper); }
  .front-panel {
    position: relative; width: 1200px; height: 2496px; overflow: hidden;
    background: linear-gradient(180deg, var(--white) 0%, var(--paper) 60%, #fbf4f6 100%);
  }
  .tagline {
    position: absolute; top: 820px; left: 0; width: 100%; text-align: center;
    font-family: "Cormorant Garamond", serif; font-weight: 500;
    font-size: 62px; letter-spacing: 2px; color: var(--navy);
  }
  .brand-name {
    position: absolute; top: 930px; left: 0; width: 100%; text-align: center;
    font-family: "Cormorant Garamond", serif; font-weight: 600;
    font-size: 240px; line-height: 1; letter-spacing: 12px; color: var(--navy);
  }
  .brand-rule { position: absolute; top: 1195px; left: 170px; width: 860px; height: 30px; }
  .product-type {
    position: absolute; top: 1245px; left: 0; width: 100%; text-align: center;
    font-family: "Noto Serif JP", serif; font-weight: 500; line-height: 1.2;
    font-size: 56px; letter-spacing: 4px; color: var(--navy);
  }
  .peach-art {
    position: absolute; left: 720px; top: 1470px; width: 420px; height: 420px; border-radius: 50%;
    background: radial-gradient(circle at 40% 35%, var(--peach-light) 0%, var(--peach-mid) 60%, var(--pink) 100%);
  }
  .ingredient-ribbon {
    position: absolute; height: 72px; line-height: 72px; text-align: center; white-space: nowrap;
    background: var(--pink-soft); color: var(--pink-deep);
    font-family: "Noto Serif JP", serif; font-weight: 700; font-size: 38px;
  }
  .ribbon-collagen { left: 120px; top: 1500px; width: 500px; transform: rotate(-8deg); }
  .ribbon-silica { left: 610px; top: 1440px; width: 530px; transform: rotate(-10deg); }
  .texture-badge {
    position: absolute; left: 170px; top: 1650px; width: 380px; height: 380px; border-radius: 50%;
    background: var(--pink-soft); border: 6px solid var(--white);
    box-shadow: 0 0 0 6px var(--pink-soft);
    display: flex; flex-direction: column; align-items: center; justify-content: center;
    font-family: "Kosugi Maru", sans-serif; color: var(--white);
  }
  .texture-badge .texture { font-size: 46px; -webkit-text-stroke: 2px var(--pink); margin-bottom: 12px; transform: rotate(-8deg); }
  .texture-badge .juice { font-size: 70px; text-shadow: 0 0 6px var(--pink-deep); }
  .texture-badge .flavor {
    margin-top: 14px; padding: 4px 32px; border-radius: 40px;
    background: var(--pink); font-size: 46px;
  }
  .volume {
    position: absolute; right: 100px; top: 2230px;
    font-family: "Cormorant Garamond", serif; font-weight: 600;
    font-size: 88px; color: var(--navy);
  }
</style>
</head>
<body>
<main class="front-panel">
  <p class="tagline">Hyaluronic beauty beverage</p>
  <h1 class="brand-name">MAKIRO</h1>
  <svg class="brand-rule" viewBox="0 0 860 30" aria-hidden="true">
    <path d="M10 18 Q430 2 850 18" fill="none" stroke="var(--navy)" stroke-width="4"/>
  </svg>
  <p class="product-type">ヒアルロン酸入りゼリー飲料</p>

  <div class="peach-art" role="img" aria-label="ピンクの桃のイラスト"></div>

  <p class="ingredient-ribbon ribbon-silica">シリカ・食物繊維・桃果汁</p>
  <p class="ingredient-ribbon ribbon-collagen">コラーゲン・ビタミンC</p>

  <div class="texture-badge">
    <span class="texture">プルプル食感</span>
    <span class="juice">果汁00%</span>
    <span class="flavor">ピーチ味</span>
  </div>

  <p class="volume">300ml</p>
</main>
</body>
</html>
```